Fitness Website for Men to purchase a book written by a Sexy Female Trainer

Keep it simple. One page. Design a Sexy website selling a Fitness book for Men Authored by a Female Fitness Trainer. Ideas attached. Word doc attached but Text and copy will change. I'm looking for an overall creative sexy design appealing to men.

Target Market(s)

Men

Industry/Entity Type

Mens Fitness & Excercise

Number of Pages Required

1 page

Colors
EE7325
F08F49
F5BC92
FAE3D3
FDF4ED
EB3D1F
EC4F4E
F09395
F8D3D4
FCEDEE

Requirements
Must have
• When men are aroused they BUY. Must be sexy. "Kelvora" Buy book Link
Nice to have
• I have included numerous attachments, Use them or not It's up to you. The design is up to you.

```html
<!DOCTYPE html>
<html lang="en">
<head>
<meta charset="utf-8">
<title>Heat &amp; Iron Club</title>
<link rel="stylesheet" href="https://fonts.googleapis.com/css2?family=Barlow+Semi+Condensed:wght@600;700&family=Montserrat:wght@600;700&family=Roboto:wght@400&family=Open+Sans:wght@400&display=swap">
<style>
  :root {
    --orange: #EE7325;
    --orange-soft: #F08F49;
    --red: #EB3D1F;
    --rose: #EC4F4E;
    --cream: #FDF4ED;
    --ink: #111111;
    --dark: #0d0d0d;
    --mist: #eeeeee;
    --white: #ffffff;
  }
  * { box-sizing: border-box; margin: 0; padding: 0; }
  html, body { width: 935px; height: 1200px; overflow: hidden; background: var(--white); }
  body { position: relative; font-family: "Roboto", sans-serif; color: var(--ink); }

  .hero { position: absolute; left: 0; top: 0; width: 935px; height: 275px;
    background: radial-gradient(ellipse at 55% 40%, #2c2c2c 0%, #151515 55%, var(--dark) 100%); }
  .hero-strip { position: absolute; left: 0; top: 275px; width: 935px; height: 37px; background: var(--mist); }
  .hero-title { position: absolute; left: 110px; top: 38px; width: 330px;
    font-family: "Barlow Semi Condensed", sans-serif; font-weight: 700; font-size: 28px;
    line-height: 33px; color: var(--white); text-transform: uppercase; letter-spacing: 0.2px; }
  .hero-title .accent { color: var(--orange); }
  .hero-actions { position: absolute; left: 110px; top: 190px; display: flex; gap: 12px; }
  .pill { display: flex; align-items: center; justify-content: center; gap: 7px; height: 40px;
    border-radius: 20px; font-family: "Montserrat", sans-serif; font-weight: 700; font-size: 12px;
    color: var(--white); letter-spacing: 0.3px; text-transform: uppercase; white-space: nowrap; }
  .pill-solid { width: 137px; background: var(--orange); }
  .pill-outline { width: 176px; border: 2px solid var(--white); font-size: 11px; }
  .pill svg { width: 16px; height: 16px; flex: none; }

  .trainer-photo { position: absolute; left: 405px; top: 0; width: 200px; height: 275px;
    background: linear-gradient(180deg, #3a3430 0%, #5a4a40 40%, #2d3b55 75%, #1b1b1b 100%); opacity: 0.85; }
  .book { position: absolute; background: linear-gradient(160deg, #d7334a 0%, #c21f3b 60%, #a3162e 100%);
    box-shadow: 6px 8px 14px rgba(0,0,0,0.35); }
  .book-back { left: 762px; top: 42px; width: 82px; height: 240px; }
  .book-front { left: 590px; top: 18px; width: 160px; height: 282px; }
  .book-front::after, .book-back::after { content: ""; position: absolute; right: -8px; top: 4px; width: 8px; height: 96%;
    background: linear-gradient(90deg, #f2f2f2, #cfcfcf); }

  .section { position: absolute; left: 0; width: 935px; text-align: center; }
  .intro { top: 312px; height: 389px; background: var(--white); }
  .story { top: 701px; height: 454px; background: var(--cream); }
  .section-title { font-family: "Montserrat", sans-serif; font-weight: 700; font-size: 24.5px;
    line-height: 30px; color: var(--ink); margin: 0 auto; }
  .section-copy { font-size: 11.3px; line-height: 18.7px; color: #222; width: 716px; }
  .section-subtitle { font-family: "Montserrat", sans-serif; font-weight: 700; font-size: 16px;
    line-height: 22px; width: 720px; }

  .intro .section-title { position: absolute; left: 0; right: 0; top: 38px; width: 660px; }
  .intro .copy-1 { position: absolute; left: 109px; top: 106px; }
  .intro .copy-2 { position: absolute; left: 109px; top: 150px; }
  .intro .section-subtitle { position: absolute; left: 107px; top: 203px; }
  .story .section-title { position: absolute; left: 0; right: 0; top: 62px; width: 690px; }
  .story .copy-1 { position: absolute; left: 109px; top: 192px; }
  .story .copy-2 { position: absolute; left: 109px; top: 256px; }

  .cta { position: absolute; left: 359px; width: 220px; height: 53px; border-radius: 27px;
    background: linear-gradient(90deg, var(--red) 0%, var(--orange) 55%, #f59a3a 100%);
    display: flex; align-items: center; justify-content: center; gap: 9px;
    font-family: "Barlow Semi Condensed", sans-serif; font-weight: 700; font-size: 20px; color: var(--white); }
  .intro .cta { top: 270px; }
  .story .cta { top: 336px; }

  .footer { position: absolute; left: 0; top: 1155px; width: 935px; height: 45px; background: #000;
    display: flex; align-items: center; justify-content: center;
    font-family: "Open Sans", sans-serif; font-size: 10px; color: #e8e8e8; }
</style>
</head>
<body>
  <header class="hero">
    <div class="trainer-photo" role="img" aria-label="Photo of a female trainer spotting a man on a bench press in a gym"></div>
    <div class="book book-back" role="img" aria-label="Second copy of the book cover"></div>
    <div class="book book-front" role="img" aria-label="Book cover: Fired Up &amp; Fit"></div>
    <h1 class="hero-title">Let’s get <span class="accent">hot, sweaty, &amp; hard together.</span> So you’re satisfied, exhausted and begging for more</h1>
    <div class="hero-actions">
      <a class="pill pill-solid">Buy Now
        <svg viewBox="0 0 16 16" fill="none" stroke="#fff" stroke-width="1.6"><circle cx="8" cy="8" r="7"/><path d="M4.5 8h6.5M8.5 5l3 3-3 3"/></svg>
      </a>
      <a class="pill pill-outline">Kelvora Buy Now
        <svg viewBox="0 0 16 16" fill="none" stroke="#fff" stroke-width="1.6"><circle cx="8" cy="8" r="7"/><path d="M4.5 8h6.5M8.5 5l3 3-3 3"/></svg>
      </a>
    </div>
  </header>
  <div class="hero-strip"></div>

  <section class="section intro">
    <h2 class="section-title">Let’s Get Hot, Sweaty, &amp; Hard Together. So You’re Satisfied, Exhausted And Begging For More</h2>
    <p class="section-copy copy-1">I’ve been using eye candy to get guys interested in health and fitness since the day I walked in the gym and turned heads.&nbsp; I figured if you wanted Tits &amp; Ass I’d give it to you.&nbsp; At least long enough to make a buck and get my guys in shape.</p>
    <p class="section-copy copy-2">As a personal fitness trainer I discovered what works for one of you doesn’t work for all of you… but when you find what works specifically for You.… WOW…the pounds melt away, your gut shrinks, and your health improves.</p>
    <h3 class="section-subtitle">This Book Has Dozens Of Real Life Success Stories From Real Guys With Real Results, All Of Them Doing Something Differently Than The Other.</h3>
    <a class="cta">BUY NOW <span>Kelvora</span></a>
  </section>

  <section class="section story">
    <h2 class="section-title">I Found What Worked For One Guy Doesn't Work For Everybody. In My Book I Have Dozens of Different Ways My Guys Got In Shape, Lost Weight, And Greatly Improved Their Health.</h2>
    <p class="section-copy copy-1">Here's a little secret about my book. A couple of my guys inspired me to write this little book.&nbsp; They thought I should capture my years of experience; tips, advice, stories, and testimonials.&nbsp; I really appreciate their encouragement. It will be fun if I sell a few books but I'm really selling this book online to gain experience. This is something I never thought I’d do.</p>
    <p class="section-copy copy-2">I said spent so many years in the gym helping my guys that trying something new sounded fun &amp; exciting. So I wrote the book and they helped me post it on Kelvora. I hope you'll purchase my little book and help me continue my journey Helping Guys get in Shape.<br>wish you all the best.&nbsp; Stay, Hot, Sweaty &amp; Hard,</p>
    <a class="cta">BUY NOW <span>Kelvora</span></a>
  </section>

  <footer class="footer">Copyright © 2023 HEAT &amp; IRON CLUB. All Rights Reserved.</footer>
</body>
</html>
```